Amber Hollow Productions

I need a business card design for a new freelance film production company using or incorporating the logo:
I want the card to be creative, minimal, yet professional. Feel free to use a variety of different shapes and sizes/ textures for the card.

Industry/Entity Type

Film Production

```html
<!DOCTYPE html>
<html lang="en">
<head>
<meta charset="utf-8">
<title>Amber Hollow Productions – Business Card</title>
<link rel="stylesheet" href="https://fonts.googleapis.com/css2?family=Open+Sans:wght@400;700&display=swap">
<style>
  :root {
    --brand-blue: #1047fb;
    --brand-tint-light: #e4eaff;
    --brand-tint-mid: #a9bdfd;
    --ink: #2a2a2a;
    --paper: #ffffff;
  }
  html, body {
    margin: 0;
    padding: 0;
    width: 1200px;
    height: 720px;
    overflow: hidden;
    background: var(--paper);
  }
  .card {
    position: relative;
    width: 1200px;
    height: 720px;
    background: var(--paper);
    font-family: "Open Sans", Arial, sans-serif;
  }
  .emblem-area {
    position: absolute;
    left: 115px;
    top: 162px;
    width: 353px;
    height: 275px;
    background: linear-gradient(180deg, var(--brand-tint-light) 0%, var(--brand-tint-mid) 100%);
  }
  .brand-band {
    position: absolute;
    left: 0;
    top: 0;
    width: 1200px;
    height: 720px;
  }
  .name-plate {
    position: absolute;
    left: 123px;
    top: 455px;
    width: 340px;
    height: 87px;
    background: var(--paper);
    display: flex;
    align-items: center;
    justify-content: center;
  }
  .company-name {
    margin: 0;
    color: var(--brand-blue);
    font-weight: 700;
    font-size: 29px;
    line-height: 1.1;
    text-align: center;
    letter-spacing: 0.5px;
  }
  .contact {
    position: absolute;
    left: 701px;
    top: 440px;
    margin: 0;
    font-style: normal;
    color: var(--ink);
    font-weight: 700;
    font-size: 27px;
    line-height: 33px;
    letter-spacing: -0.3px;
  }
  .contact-line {
    display: block;
    white-space: nowrap;
  }
  .contact-label {
    color: var(--brand-blue);
  }
</style>
</head>
<body>
  <main class="card">
    <div class="emblem-area" role="img" aria-label="Company emblem: city skyline above a film strip"></div>

    <svg class="brand-band" viewBox="0 0 1200 720" aria-hidden="true">
      <path d="M115 446 H526 L673 598 H137 Q115 598 115 576 Z" fill="var(--brand-blue)"/>
    </svg>

    <div class="name-plate">
      <p class="company-name">Amber Hollow<br>Productions</p>
    </div>

    <address class="contact">
      <span class="contact-line">Street name 1111</span>
      <span class="contact-line">Area, City</span>
      <span class="contact-line"><span class="contact-label">Tel:</span> +00001111 44 77</span>
      <span class="contact-line">myname@yourcompany.com</span>
      <span class="contact-line">www.amberhollow.demo</span>
    </address>
  </main>
</body>
</html>
```